LANTERN DIVE

IM LOOKING AT A BROCHURE MY MY DIVE CENTRE WE DO COURSES FROM INTRO TO PROFESSIONAL, IM OPEN TO DESIGN AND COLOURS, JUST LOOKING FOR SOMETHING THAT STANDS OUT.

i HAVE INCLUDED A COPY OF OUR LAST BROCHURE SO YOU CAN SEE THE INFORMATION THAT WE PREVIOUSLY USED AND ALSO OUR PRICING.

WE HAVE MANY DIVE COMPANY'S IN NORTH QUEENSLAND AND THROUGHOUT AUSTRALIA, WE ARE AFTER SOMETHING THAT PEOPLE ARE DRAWN TO AND WILL STAND OUT AMONGST OTHER COMPETITORS.

LOOKING FOR PLAYFUL AND FUN

```html
<!DOCTYPE html>
<html lang="en">
<head>
<meta charset="utf-8">
<title>Lantern Dive – Tri-fold Brochure</title>
<link href="https://fonts.googleapis.com/css2?family=Open+Sans:wght@400;600;700;800&display=swap" rel="stylesheet">
<style>
  :root {
    --bg: #8c9ea8;
    --ocean: #1ea0e4;
    --ocean-light: #cfe8f7;
    --ocean-pale: #e6f3fb;
    --deep: #0b3f8c;
    --ink: #222222;
    --band: #262626;
    --paper: #f2f2f2;
    --white: #ffffff;
    --ring: #9a9a9a;
    --muted: #6b6b6b;
  }
  * { box-sizing: border-box; margin: 0; padding: 0; }
  html, body { width: 1200px; height: 858px; overflow: hidden; }
  body {
    background: var(--bg);
    font-family: "Open Sans", Arial, sans-serif;
    display: flex; align-items: center; justify-content: center;
  }
  .brochure {
    width: 1020px; height: 720px;
    display: flex;
    box-shadow: 0 20px 40px rgba(0,0,0,.25);
  }
  .panel { width: 340px; height: 100%; position: relative; display: flex; flex-direction: column; }
  .panel-body { flex: 1; position: relative; }
  .footer-band {
    height: 80px; background: var(--band); color: var(--white);
    display: flex; align-items: center; justify-content: center; gap: 14px;
    font-size: 15px;
  }

  /* Panel 1 – certification */
  .panel-certify { background: var(--ocean); color: var(--white); }
  .panel-certify .panel-body { padding: 50px 30px 20px; text-align: center; }
  .certify-title { font-size: 26px; font-weight: 800; letter-spacing: 1px; margin-bottom: 16px; }
  .certify-text { font-size: 15px; line-height: 1.45; margin-bottom: 14px; }
  .certify-text strong { font-weight: 700; }
  .hours-table {
    width: 100%; border-collapse: collapse; margin-top: 20px;
    font-size: 13px; color: var(--ocean); text-align: left;
  }
  .hours-table th { font-weight: 700; padding: 6px 10px; background: var(--white); }
  .hours-table td { padding: 5px 10px; }
  .hours-table tr:nth-child(odd) td { background: var(--ocean-light); }
  .hours-table tr:nth-child(even) td { background: var(--ocean-pale); }
  .hours-table td + td, .hours-table th + th { border-left: 2px solid var(--ocean); }
  .certify-phone { margin-top: 30px; font-size: 17px; font-weight: 700; }
  .footer-band .call-out { font-style: italic; font-weight: 700; }

  /* Panel 2 – contact */
  .panel-contact { background: var(--paper); }
  .panel-contact .panel-body { padding: 120px 30px 0; text-align: center; }
  .name-badge {
    width: 150px; height: 150px; border-radius: 50%;
    border: 3px solid var(--ring); background: var(--white);
    margin: 0 auto 34px; display: flex; align-items: center; justify-content: center;
    font-size: 20px; font-weight: 600; color: var(--muted);
  }
  .contact-name { font-size: 28px; font-weight: 700; color: var(--ocean); margin-bottom: 14px; }
  .contact-address { font-size: 15px; line-height: 1.5; color: var(--ink); }
  .contact-line { font-size: 15px; line-height: 1.5; color: var(--ocean); }
  .social-dot {
    width: 30px; height: 30px; border-radius: 50%; background: var(--ocean);
    flex: none;
  }
  .social-url { color: var(--ocean); font-size: 14px; }

  /* Panel 3 – cover */
  .panel-cover { background: var(--ocean); }
  .cover-photo {
    position: absolute; left: 0; top: 0; width: 340px; height: 420px;
  }
  .cover-name-badge {
    position: absolute; left: 40px; top: 330px;
    width: 160px; height: 160px; border-radius: 50%; background: var(--white);
    display: flex; align-items: center; justify-content: center;
    font-size: 21px; font-weight: 600; color: var(--muted);
  }
  .cover-headline {
    position: absolute; left: 30px; bottom: 30px; right: 30px;
    color: var(--white); font-size: 27px; font-weight: 800; line-height: 1.15;
  }
  .cover-url { font-size: 19px; font-weight: 700; letter-spacing: .5px; }
</style>
</head>
<body>
  <main class="brochure">
    <section class="panel panel-certify">
      <div class="panel-body">
        <h2 class="certify-title">GET CERTIFIED</h2>
        <p class="certify-text">4 day Open Water Dive Course including 4 nights accomodation <strong>only $399.00</strong>.</p>
        <p class="certify-text">Weekly courses commencing on the following days: Monday, Thursday &amp; Saturdays.</p>
        <table class="hours-table">
          <thead><tr><th>Day</th><th>Opening Hours</th></tr></thead>
          <tbody>
            <tr><td>Monday</td><td>09.00am - 4.30pm</td></tr>
            <tr><td>Tuesday</td><td>09.00am - 4.30pm</td></tr>
            <tr><td>Wednesday</td><td>09.00am - 4.30pm</td></tr>
            <tr><td>Thursday</td><td>09.00am - 4.30pm</td></tr>
            <tr><td>Friday</td><td>09.00am - 4.30pm</td></tr>
            <tr><td>Saturday</td><td>09.00am - 4.30pm</td></tr>
            <tr><td>Sunday</td><td>09.00am - 4.30pm</td></tr>
          </tbody>
        </table>
        <p class="certify-phone">Phone: +61 400 118 276</p>
      </div>
      <footer class="footer-band"><span class="call-out">Call us today!</span></footer>
    </section>

    <section class="panel panel-contact">
      <div class="panel-body">
        <div class="name-badge">Lantern Dive</div>
        <h2 class="contact-name">Lantern Dive</h2>
        <p class="contact-address">12 Coral Cove Rd, Palm Bay,<br>Reef Island, 4800 Queensland</p>
        <p class="contact-line">info@lanterndive.com.au</p>
        <p class="contact-line">Phone: +61 400 118 276</p>
      </div>
      <footer class="footer-band">
        <span class="social-dot"></span>
        <span class="social-url">www.facebook.com/lanterndiveau</span>
      </footer>
    </section>

    <section class="panel panel-cover">
      <div class="panel-body">
        <svg class="cover-photo" viewBox="0 0 340 420" role="img" aria-label="Underwater photo of a scuba diver swimming among manta rays in deep blue water">
          <defs>
            <linearGradient id="sea" x1="0" y1="0" x2="0" y2="1">
              <stop offset="0" stop-color="#4aa3e6"/>
              <stop offset=".55" stop-color="#1560b8"/>
              <stop offset="1" stop-color="#0b3f8c"/>
            </linearGradient>
          </defs>
          <path d="M0 0 H340 V330 Q200 420 0 430 Z" fill="url(#sea)"/>
        </svg>
        <div class="cover-name-badge">Lantern Dive</div>
        <h1 class="cover-headline">Become a Certified Open Water diver for only $350!</h1>
      </div>
      <footer class="footer-band"><span class="cover-url">www.lanterndive.com.au</span></footer>
    </section>
  </main>
</body>
</html>
```